Vorin Co Premium Matcha brand Label

This is a label design project for a luxury tea brand. Feel free to be creative within the guidelines.
Attached to this project is a document called “Private Label Design Requirements” with the design guidelines and template. There is another document called "Vorin Co Packaging Instructions" this has more details necessary to stick to the guidelines in the first document.

I have also attached the certifications to be included as well as different variations of the logo for you to use.

If you have any questions, I am here.

Need extra days to review

Young, active, fun, enjoy the finer things

```html
<!DOCTYPE html>
<html lang="en">
<head>
<meta charset="utf-8">
<title>Vorin Co Premium Matcha Label</title>
<link rel="stylesheet" href="https://fonts.googleapis.com/css2?family=Raleway:wght@600;700;800&display=swap">
<style>
  :root {
    --backdrop-light: #bdc9b9;
    --backdrop-dark: #95ad8a;
    --leaf-deep: #1f5a1a;
    --leaf-mid: #3f8f2a;
    --leaf-bright: #7cc446;
    --olive: #4a5f22;
    --olive-ring: #3f5a1f;
    --fresh: #6ab84a;
    --heading-lime: #b2d146;
    --white: #ffffff;
    --ink: #222222;
    --badge-green: #1f7a3a;
    --badge-teal: #2b7fa0;
  }
  * { box-sizing: border-box; margin: 0; padding: 0; }
  html, body { width: 1200px; height: 803px; overflow: hidden; }
  body {
    position: relative;
    font-family: "Raleway", sans-serif;
    background: var(--backdrop-light);
  }
  .backdrop { position: absolute; inset: 0; width: 1200px; height: 803px; }

  .label {
    position: absolute;
    left: 51px;
    width: 1098px;
    height: 214px;
    overflow: hidden;
    box-shadow: 0 6px 10px rgba(0,0,0,0.25);
  }
  .label--top { top: 166px; }
  .label--bottom { top: 436px; }

  .label__photo {
    position: absolute; inset: 0;
    background:
      radial-gradient(ellipse at 20% 30%, var(--leaf-bright) 0%, transparent 45%),
      radial-gradient(ellipse at 75% 70%, var(--leaf-bright) 0%, transparent 40%),
      radial-gradient(ellipse at 50% 10%, var(--leaf-mid) 0%, transparent 50%),
      linear-gradient(135deg, var(--leaf-mid) 0%, var(--leaf-deep) 50%, var(--leaf-mid) 100%);
  }

  .distributor {
    position: absolute;
    left: 0; top: 109px;
    width: 283px; height: 63px;
    border-radius: 0 32px 32px 0;
    background: var(--olive);
    color: var(--white);
    padding: 7px 0 0 76px;
    font-size: 10px;
    font-weight: 600;
    line-height: 16px;
  }

  .seal {
    position: absolute;
    left: 467px; top: 23px;
    width: 166px; height: 166px;
    border-radius: 50%;
    background: var(--white);
  }
  .seal__ring {
    position: absolute;
    left: 18px; top: 18px;
    width: 130px; height: 130px;
    border-radius: 50%;
    border: 2px solid var(--olive-ring);
  }
  .seal__brand {
    position: absolute;
    left: 0; right: 0; top: 60px;
    text-align: center;
    font-size: 15px;
    font-weight: 800;
    color: var(--ink);
  }
  .seal__dot {
    position: absolute;
    left: 71px; top: 32px;
    width: 24px; height: 24px;
    border-radius: 50%;
    background: var(--fresh);
  }
  .seal__band {
    position: absolute;
    left: 4px; right: 4px; top: 100px;
    height: 35px;
    background: var(--olive);
    color: var(--white);
    text-align: center;
    font-size: 11.5px;
    font-weight: 700;
    line-height: 14px;
    padding-top: 4px;
  }
  .seal__weight {
    position: absolute;
    left: 0; right: 0; top: 137px;
    text-align: center;
    font-size: 7px;
    font-weight: 700;
    color: var(--ink);
  }

  .info {
    position: absolute;
    left: 777px; top: 0;
    width: 244px; height: 194px;
    border-radius: 0 0 40px 44px;
    background: var(--olive);
    color: var(--white);
    padding: 35px 0 0 6px;
  }
  .info__heading {
    font-size: 12px;
    font-weight: 700;
    color: var(--heading-lime);
    line-height: 16px;
  }
  .info__text {
    font-size: 10px;
    font-weight: 700;
    padding-left: 8px;
    line-height: 13px;
    margin: 1px 0 13px;
  }
  .info__steps { list-style: none; padding-left: 8px; font-size: 9.5px; font-weight: 700; line-height: 12px; margin-top: 1px; }
  .info__steps li::before { content: "\2022\00a0"; }
  .badges { position: absolute; left: 141px; top: 141px; display: flex; gap: 5px; align-items: center; }
  .badge--round { width: 31px; height: 31px; border-radius: 50%; background: var(--badge-green); border: 2px solid var(--white); }
  .badge--square { width: 36px; height: 28px; background: var(--badge-teal); border: 2px solid var(--white); }

  .label--light .distributor,
  .label--light .info { background: var(--fresh); }
  .label--light .info__heading { color: var(--white); }
</style>
</head>
<body>
  <svg class="backdrop" viewBox="0 0 1200 803" aria-hidden="true">
    <rect width="1200" height="803" fill="var(--backdrop-light)"/>
    <polygon points="0,763 1200,0 1200,803 0,803" fill="var(--backdrop-dark)"/>
  </svg>

  <section class="label label--top">
    <div class="label__photo" role="img" aria-label="Close-up photograph of fresh green tea leaves"></div>
    <div class="distributor">
      <p>Distributed by Vorin Co. | Marlow, Ky</p>
      <p>Certified Organic by Qesta</p>
      <p>PRODUCT OF JAPAN</p>
    </div>
    <div class="seal">
      <div class="seal__ring"></div>
      <div class="seal__dot"></div>
      <p class="seal__brand">Vorin Co</p>
      <p class="seal__band">PREMIUM ORGANIC<br>CEREMONIAL MATCHA</p>
      <p class="seal__weight">Net Wt: 30g</p>
    </div>
    <div class="info">
      <h2 class="info__heading">Ingredients</h2>
      <p class="info__text">Premium Organic Japanese Matcha Green Tea</p>
      <h2 class="info__heading">Instructions</h2>
      <ul class="info__steps">
        <li>2 tsp of Matcha</li>
        <li>2oz of Water (170-180 degrees F)</li>
        <li>Whisk in a W formation until frothy</li>
        <li>Sweeten to taste</li>
      </ul>
      <div class="badges">
        <span class="badge badge--round" role="img" aria-label="Organic certification badge"></span>
        <span class="badge badge--square" role="img" aria-label="Non-GMO verification badge"></span>
      </div>
    </div>
  </section>

  <section class="label label--bottom label--light">
    <div class="label__photo" role="img" aria-label="Close-up photograph of fresh green tea leaves"></div>
    <div class="distributor">
      <p>Distributed by Vorin Co. | Marlow, Ky</p>
      <p>Certified Organic by Qesta</p>
      <p>PRODUCT OF JAPAN</p>
    </div>
    <div class="seal">
      <div class="seal__ring"></div>
      <div class="seal__dot"></div>
      <p class="seal__brand">Vorin Co</p>
      <p class="seal__band">PREMIUM ORGANIC<br>CEREMONIAL MATCHA</p>
      <p class="seal__weight">Net Wt: 30g</p>
    </div>
    <div class="info">
      <h2 class="info__heading">Ingredients</h2>
      <p class="info__text">Premium Organic Japanese Matcha Green Tea</p>
      <h2 class="info__heading">Instructions</h2>
      <ul class="info__steps">
        <li>2 tsp of Matcha</li>
        <li>2oz of Water (170-180 degrees F)</li>
        <li>Whisk in a W formation until frothy</li>
        <li>Sweeten to taste</li>
      </ul>
      <div class="badges">
        <span class="badge badge--round" role="img" aria-label="Organic certification badge"></span>
        <span class="badge badge--square" role="img" aria-label="Non-GMO verification badge"></span>
      </div>
    </div>
  </section>
</body>
</html>
```